Facial Tissue Brand Logo and Design

We would like you to design a Logo for the Facial Tissue Brand "Velora" along with the box design. The pack should indicate the pack size (150 x 2 ply). Also our company logo should be present (attached) along with a barcode. The box size dimensions should be 210mm (L) x 110mm (W) x 70mm (H). We are open to all kinds of nice designs which are attractive but not overdone. Happy designing!

UPDATE:
We appreciate the designs so far... but would also love to see more options in a simple and elegent design style that would look good on a table... please see attached below links for reference purpose:

www.pixmarrow.com/image-photo/cleaning-wipes-isolated-on-white-480215736

www.pixmarrow.com/image-photo/cleaning-wipes-isolated-on-white-692048153

www.pixmarrow.com/image-photo/delicate-female-hands-pulling-tissue-out-2875013649

Happy desgining!

We appreciate the designs so far.. but would like to to see some more options.

```html
<!DOCTYPE html>
<html lang="en">
<head>
<meta charset="utf-8">
<title>Velora Facial Tissue – Box Panels</title>
<link rel="stylesheet" href="https://fonts.googleapis.com/css2?family=Rubik:wght@400;500;700&display=swap">
<style>
  :root {
    --canvas: #ffffff;
    --sky-light: #f4fbff;
    --sky-mid: #bfe4f7;
    --sky-deep: #7cc6ec;
    --navy: #1d4f9a;
    --royal: #2a6fb8;
    --leaf-dark: #1c5aa6;
    --leaf-teal: #3aa7cf;
    --edge: #8aa9bf;
    --ink: #222222;
  }
  * { margin: 0; padding: 0; box-sizing: border-box; }
  html, body { width: 1200px; height: 1000px; overflow: hidden; background: var(--canvas); }
  body { position: relative; font-family: "Rubik", Arial, sans-serif; }

  .dimensions {
    position: absolute; left: 950px; top: 263px;
    font-size: 11px; color: var(--ink); letter-spacing: 0.1px;
  }

  .panel {
    position: absolute; overflow: hidden;
    border: 1px solid var(--edge);
    background: radial-gradient(ellipse at 55% 30%, var(--sky-light) 0%, var(--sky-mid) 55%, var(--sky-deep) 100%);
  }
  .panel--end  { left: 491px; top: 284px; width: 165px; height: 260px; }
  .panel--top  { left: 661px; top: 284px; width: 493px; height: 260px; }
  .panel--side { left: 661px; top: 548px; width: 493px; height: 165px; }

  .foliage {
    position: absolute;
    background:
      radial-gradient(ellipse at 20% 95%, rgba(28,90,166,0.95) 0%, rgba(42,111,184,0.7) 30%, rgba(58,167,207,0.45) 55%, rgba(124,198,236,0) 80%);
  }
  .panel--top .foliage  { left: 0; top: 90px; width: 280px; height: 170px; }
  .panel--side .foliage { left: 0; top: 20px; width: 220px; height: 145px; }
  .panel--end .foliage  {
    left: 0; top: 0; width: 110px; height: 110px;
    background: radial-gradient(ellipse at 0% 15%, rgba(28,90,166,0.9) 0%, rgba(58,167,207,0.5) 45%, rgba(124,198,236,0) 80%);
  }

  .brand { position: absolute; text-align: center; color: var(--navy); }
  .brand__name { font-weight: 700; line-height: 1; display: flex; align-items: center; justify-content: center; gap: 10px; }
  .brand__dot { width: 12px; height: 12px; border-radius: 50%; background: var(--navy); flex: none; }
  .brand__type { font-weight: 400; color: var(--royal); letter-spacing: 1px; margin-top: 6px; }

  .panel--top .brand  { left: 150px; top: 48px; width: 260px; }
  .panel--top .brand__name { font-size: 50px; }
  .panel--top .brand__type { font-size: 17px; }

  .panel--side .brand { left: 150px; top: 40px; width: 200px; }
  .panel--side .brand__name { font-size: 36px; }
  .panel--side .brand__dot { width: 9px; height: 9px; }
  .panel--side .brand__type { font-size: 13px; margin-top: 4px; }

  .panel--end .brand {
    left: -40px; top: 110px; width: 240px;
    transform: rotate(72deg);
  }
  .panel--end .brand__name { font-size: 32px; }
  .panel--end .brand__dot { width: 8px; height: 8px; }
  .panel--end .brand__type { font-size: 11px; margin-top: 3px; }

  .pack-info { position: absolute; left: 322px; top: 203px; color: var(--navy); }
  .pack-info__count { font-size: 15px; font-weight: 700; }
  .pack-info__ply { font-size: 8px; margin-top: 2px; }
  .pack-info__note { font-size: 6px; margin-top: 2px; color: var(--navy); }

  .company {
    position: absolute; left: 345px; top: 104px;
    display: flex; align-items: center; gap: 7px;
    color: var(--royal); font-size: 12px; font-weight: 400; line-height: 1.1;
  }
  .company__square { width: 22px; height: 22px; background: var(--royal); flex: none; }
</style>
</head>
<body>
  <p class="dimensions">210mm (L) x 110mm (W) x 70mm (H)</p>

  <section class="panel panel--end" aria-label="End panel">
    <div class="foliage" role="img" aria-label="Layered translucent blue leaf illustration"></div>
    <div class="brand">
      <div class="brand__name"><span class="brand__dot"></span>Velora</div>
      <div class="brand__type">FACIAL TISSUE</div>
    </div>
  </section>

  <section class="panel panel--top" aria-label="Top panel">
    <div class="foliage" role="img" aria-label="Layered translucent blue leaf illustration"></div>
    <div class="brand">
      <div class="brand__name"><span class="brand__dot"></span>Velora</div>
      <div class="brand__type">FACIAL TISSUE</div>
    </div>
    <div class="pack-info">
      <p class="pack-info__count">150 Sheets</p>
      <p class="pack-info__ply">2 Ply Soft &amp; Absorbent Facial Tissues</p>
      <p class="pack-info__note">Made from 100% recycled paper</p>
    </div>
  </section>

  <section class="panel panel--side" aria-label="Side panel">
    <div class="foliage" role="img" aria-label="Layered translucent blue leaf illustration"></div>
    <div class="brand">
      <div class="brand__name"><span class="brand__dot"></span>Velora</div>
      <div class="brand__type">FACIAL TISSUE</div>
    </div>
    <div class="company">
      <span class="company__square"></span>
      <span>Norvane Trading FZC</span>
    </div>
  </section>
</body>
</html>
```